Stationary
Vela Rigs
Use same font as used in my logo
Use a complement to the logo font
Professional
Tom Baxter
Owner/Installation Consultant
5678 Halloway Dr.
Clark ON, K7P 5R9
tom@velarigs.com
www.velarigs.com

```html
<!DOCTYPE html>
<html lang="en">
<head>
<meta charset="utf-8">
<title>Vela Rigs Stationery</title>
<link rel="stylesheet" href="https://fonts.googleapis.com/css2?family=Oswald:wght@500&family=Open+Sans:wght@400;600&display=swap">
<style>
:root{
  --bg:#e9e3da;
  --paper:#ffffff;
  --red:#b3161c;
  --red-dark:#7d0e12;
  --charcoal:#2b2b2b;
  --grey-light:#d7d7d7;
  --ink:#444;
  --label:#6b5a48;
}
*{margin:0;padding:0;box-sizing:border-box}
html,body{width:1200px;height:463px;overflow:hidden;background:var(--bg)}
.board{position:relative;width:1200px;height:463px;font-family:"Open Sans",Arial,sans-serif;color:var(--ink)}
.sheet{position:absolute;background:var(--paper);box-shadow:0 2px 6px rgba(0,0,0,.25);overflow:hidden}
.decor{position:absolute;inset:0;width:100%;height:100%}
.label{position:absolute;font-size:6px;letter-spacing:.8px;text-transform:uppercase;color:var(--label);font-weight:600;white-space:nowrap}
.section-title{left:19px;top:128px;font-size:7px}
.brand{position:absolute;display:flex;flex-direction:column;align-items:center;gap:3px}
.brand-dot{width:12px;height:12px;border-radius:50%;background:var(--red)}
.brand-name{font-family:"Oswald",Arial,sans-serif;font-weight:500;font-size:7px;letter-spacing:1.4px;color:var(--charcoal);text-transform:uppercase;white-space:nowrap}
.brand.on-dark .brand-name{color:#fff}
.brand-faint{position:absolute;left:0;right:0;text-align:center;font-family:"Oswald",Arial,sans-serif;font-weight:500;font-size:28px;letter-spacing:4px;color:#f1f1f1;text-transform:uppercase}
.contact{position:absolute;font-size:4.6px;line-height:7px;color:var(--ink)}
.contact strong{font-weight:600;color:var(--charcoal)}
.contact-line{position:absolute;left:0;right:0;display:flex;justify-content:center;gap:14px;font-size:4.4px;color:var(--ink);white-space:nowrap}
.card{position:absolute;width:90px;height:50px;background:var(--charcoal);box-shadow:0 2px 5px rgba(0,0,0,.35);overflow:hidden;border-radius:2px}
.card-contact{position:absolute;left:7px;top:25px;font-size:3.6px;line-height:5px;color:#ddd;white-space:nowrap}
.card-contact strong{color:#fff;font-weight:600}
.envelope{position:absolute;box-shadow:0 2px 5px rgba(0,0,0,.28);overflow:hidden}
.env-web{position:absolute;left:0;right:0;text-align:center;font-size:4.4px;color:var(--ink)}
</style>
</head>
<body>
<main class="board">

  <p class="label section-title">Stationery Concepts</p>

  <!-- business card front -->
  <div class="card card-front" style="left:19px;top:166px">
    <svg class="decor" viewBox="0 0 90 50" preserveAspectRatio="none">
      <path d="M0 40 Q40 36 90 46 L90 50 L0 50Z" fill="var(--red)"/>
      <path d="M0 44 Q40 42 90 50 L0 50Z" fill="var(--red-dark)"/>
    </svg>
    <div class="brand on-dark" style="left:7px;top:6px;flex-direction:row;gap:4px">
      <span class="brand-dot" style="width:8px;height:8px"></span>
      <span class="brand-name" style="font-size:5.5px">Vela Rigs</span>
    </div>
    <div class="card-contact">
      <strong>Tom Baxter</strong><br>Owner/Installation Consultant<br>tom@velarigs.com
    </div>
  </div>
  <p class="label" style="left:19px;top:222px">Business Card Front</p>

  <!-- business card back -->
  <div class="card card-back" style="left:19px;top:236px;background:#111">
    <svg class="decor" viewBox="0 0 90 50" preserveAspectRatio="none">
      <path d="M66 0 Q84 16 90 34 L90 0Z" fill="var(--red)"/>
    </svg>
    <div class="brand on-dark" style="left:0;right:0;top:16px">
      <span class="brand-dot" style="width:9px;height:9px"></span>
      <span class="brand-name" style="font-size:5.5px">Vela Rigs</span>
    </div>
  </div>
  <p class="label" style="left:19px;top:292px">Business Card Back</p>

  <!-- letterhead option 1 -->
  <div class="sheet letterhead" style="left:168px;top:34px;width:216px;height:386px">
    <svg class="decor" viewBox="0 0 216 386">
      <path d="M176 0 Q206 6 216 46 L216 0Z" fill="var(--grey-light)"/>
      <path d="M184 0 Q208 4 216 32 L216 0Z" fill="var(--red)"/>
      <path d="M0 330 Q6 378 48 386 L0 386Z" fill="var(--grey-light)"/>
      <path d="M0 344 Q5 380 36 386 L0 386Z" fill="var(--red)"/>
    </svg>
    <div class="brand" style="left:0;right:0;top:12px">
      <span class="brand-dot"></span>
      <span class="brand-name">Vela Rigs</span>
    </div>
    <p class="brand-faint" style="top:160px">Vela Rigs</p>
    <div class="contact" style="left:14px;top:254px">
      <strong>Tom Baxter</strong><br>Owner/Installation Consultant<br>5678 Halloway Dr.<br>Clark ON, K7P 5R9<br>Tel. 555-014-2280<br>tom@velarigs.com<br>www.velarigs.com
    </div>
  </div>
  <p class="label" style="left:228px;top:429px">Letter Head Option 1</p>

  <!-- letterhead option 2 -->
  <div class="sheet letterhead" style="left:470px;top:34px;width:216px;height:386px">
    <svg class="decor" viewBox="0 0 216 386">
      <path d="M168 0 Q206 8 216 56 L216 0Z" fill="var(--charcoal)"/>
      <path d="M178 0 Q208 6 216 38 L216 0Z" fill="var(--red)"/>
      <path d="M10 372 L206 372" stroke="var(--grey-light)" stroke-width="0.6"/>
    </svg>
    <div class="brand" style="left:0;right:0;top:12px">
      <span class="brand-dot"></span>
      <span class="brand-name">Vela Rigs</span>
    </div>
    <p class="brand-faint" style="top:160px">Vela Rigs</p>
    <p class="contact-line" style="top:376px">
      <span>5678 Halloway Dr., Clark ON, K7P 5R9</span>
      <span>tom@velarigs.com</span>
      <span>www.velarigs.com</span>
    </p>
  </div>
  <p class="label" style="left:530px;top:429px">Letter Head Option 2</p>

  <!-- envelope backs -->
  <div class="envelope" style="left:828px;top:34px;width:348px;height:58px;background:var(--red)">
    <svg class="decor" viewBox="0 0 348 58" preserveAspectRatio="none">
      <path d="M0 0 L174 42 L348 0Z" fill="var(--red-dark)"/>
    </svg>
  </div>
  <div class="envelope" style="left:828px;top:96px;width:348px;height:60px;background:var(--charcoal)">
    <svg class="decor" viewBox="0 0 348 60" preserveAspectRatio="none">
      <path d="M0 0 L174 42 L348 0Z" fill="#1a1a1a"/>
    </svg>
  </div>
  <div class="envelope" style="left:828px;top:160px;width:348px;height:96px;background:var(--paper)">
    <svg class="decor" viewBox="0 0 348 96" preserveAspectRatio="none">
      <path d="M0 0 L174 50 L348 0Z" fill="#f2f2f2" stroke="var(--grey-light)" stroke-width="0.6"/>
    </svg>
    <div class="brand" style="left:0;right:0;top:54px">
      <span class="brand-dot" style="width:9px;height:9px"></span>
      <span class="brand-name" style="font-size:6px">Vela Rigs</span>
    </div>
    <p class="env-web" style="top:84px">www.velarigs.com</p>
  </div>

  <!-- envelope front -->
  <div class="envelope" style="left:773px;top:283px;width:163px;height:113px;background:var(--paper)">
    <svg class="decor" viewBox="0 0 163 113">
      <path d="M110 113 Q148 106 163 78 L163 113Z" fill="var(--grey-light)"/>
      <path d="M124 113 Q154 106 163 90 L163 113Z" fill="var(--red)"/>
    </svg>
    <div class="brand" style="left:0;right:0;top:10px">
      <span class="brand-dot" style="width:9px;height:9px"></span>
      <span class="brand-name" style="font-size:6px">Vela Rigs</span>
    </div>
  </div>
  <p class="label" style="left:822px;top:429px">Envelope Option 1</p>

</main>
</body>
</html>
```